An international wholesale business needs letterhead design

Logo file is attached. Please design a letterhead with the following details:

- Company Name and Logo
- Address
- VAT Registration number
- Phone No
- Website address

```html
<!DOCTYPE html>
<html lang="en">
<head>
<meta charset="utf-8">
<title>Norvane Trading Letterhead</title>
<link rel="stylesheet" href="https://fonts.googleapis.com/css2?family=Oranienbaum&family=Open+Sans:wght@400;600&display=swap">
<style>
  :root {
    --backdrop: #6b6d7c;
    --paper: #f7f7f7;
    --brand-red: #c4202c;
    --brand-grey: #8e9094;
    --ink: #2b2b2b;
    --ink-soft: #555;
  }
  * { box-sizing: border-box; margin: 0; padding: 0; }
  html, body { width: 1200px; height: 800px; overflow: hidden; }
  body {
    background: var(--backdrop);
    display: flex; align-items: center; justify-content: center;
    font-family: "Oranienbaum", "Times New Roman", serif;
    color: var(--ink);
  }
  .letterhead {
    position: relative;
    width: 540px; height: 764px;
    background: var(--paper);
    box-shadow: 0 6px 18px rgba(0,0,0,.25);
    padding: 46px 46px 0;
  }
  .masthead { display: flex; align-items: center; gap: 18px; }
  .brand { display: flex; align-items: center; gap: 8px; }
  .brand-dot {
    width: 30px; height: 30px; border-radius: 50%;
    background: var(--brand-red);
  }
  .brand-name {
    font-size: 27px; color: var(--brand-red); letter-spacing: .5px;
    line-height: 1;
  }
  .divider { display: flex; gap: 4px; height: 58px; }
  .divider span { width: 1.5px; background: var(--brand-red); }
  .contact-list { list-style: none; font-family: "Open Sans", Arial, sans-serif; font-size: 7.5px; color: var(--ink-soft); }
  .contact-list li { display: flex; align-items: center; gap: 6px; line-height: 13px; }
  .contact-icon {
    width: 9px; height: 9px; border-radius: 50%; background: var(--brand-red);
    display: inline-flex; align-items: center; justify-content: center;
  }
  .doc-title { margin: 18px 0 0 292px; }
  .doc-title h2 { font-weight: 400; font-size: 15px; line-height: 1; }
  .doc-title p, .recipient p { font-size: 7.5px; color: var(--ink-soft); }
  .recipient { margin-top: 6px; }
  .recipient h2 { font-weight: 400; font-size: 15px; line-height: 1; }
  .letter-body { margin-top: 26px; font-size: 8.6px; line-height: 1.42; color: #333; text-align: justify; }
  .letter-body p + p { margin-top: 20px; }
  .signature { text-align: right; margin-top: 34px; padding-right: 10px; }
  .signature h3 { font-weight: 400; font-size: 20px; line-height: 1; }
  .signature p { font-size: 9px; color: var(--ink-soft); }
  .footer-address {
    position: absolute; left: 46px; bottom: 44px;
    font-family: "Open Sans", Arial, sans-serif; font-size: 8px; color: var(--ink-soft);
  }
  .footer-band {
    position: absolute; left: 0; right: 0; bottom: 0; height: 22px;
    background: var(--brand-red);
  }
  .footer-band .stripe { position: absolute; top: 0; bottom: 0; width: 5px; background: var(--brand-grey); }
</style>
</head>
<body>
  <main class="letterhead">
    <header class="masthead">
      <div class="brand">
        <span class="brand-dot"></span>
        <span class="brand-name">NORVANE TRADING</span>
      </div>
      <div class="divider"><span></span><span></span></div>
      <ul class="contact-list">
        <li><span class="contact-icon"></span>info@norvanetrading.com</li>
        <li><span class="contact-icon"></span>+47 555 010 234</li>
        <li><span class="contact-icon"></span>+47 555 010 235</li>
        <li><span class="contact-icon"></span>www.norvanetrading.com</li>
        <li><span class="contact-icon"></span>VAT Reg number : 000-0000-0000</li>
      </ul>
    </header>

    <section class="doc-title">
      <h2>Branding Invoice</h2>
      <p>Dated 3-10-2017</p>
    </section>

    <section class="recipient">
      <h2>Outdoor Advertisement</h2>
      <p>HR Department</p>
    </section>

    <article class="letter-body">
      <p>Lorem Ipsum is simply dummy text of the printing and typesetting industry. Lorem Ipsum has been the industry's standard dummy text ever since the 1500s, when an unknown printer took a galley of type and scrambled it to make a type specimen book. It has survived not only five centuries, but also the leap into electronic typesetting, remaining essentially unchanged. It was popularised in the 1960s with the release of Letraset sheets containing Lorem Ipsum passages, and more recently with desktop publishing software like Aldus PageMaker including versions of Lorem Ipsum.</p>
      <p>Lorem Ipsum is simply dummy text of the printing and typesetting industry. Lorem Ipsum has been the industry's standard dummy text ever since the 1500s, when an unknown printer took a galley of type and scrambled it to make a type specimen book. It has survived not only five centuries, but also the leap into electronic typesetting, remaining essentially unchanged. It was popularised in the 1960s with the release of Letraset sheets containing Lorem Ipsum passages, and more recently with desktop publishing software like Aldus PageMaker including versions of Lorem Ipsum. Lorem Ipsum is simply dummy text of the printing and typesetting industry. Lorem Ipsum has been the industry's standard dummy text ever since the 1500s, when an unknown printer took a galley of type and scrambled it to make a type specimen book. It has survived not only five centuries, but also the leap into electronic typesetting, remaining essentially unchanged. It was popularised in the 1960s with the release of Letraset sheets containing Lorem Ipsum passages, and more recently with desktop publishing software like Aldus PageMaker including versions of Lorem Ipsum. Lorem Ipsum is simply dummy text of the printing and typesetting industry. Lorem Ipsum has been the industry's standard dummy text ever since the 1500s, when an unknown printer took a galley of type and scrambled it to make a type specimen book. It has survived not only five centuries, but also the leap into electronic typesetting, remaining essentially unchanged. It was popularised in the 1960s with the release of Letraset sheets containing Lorem Ipsum passages, and more recently with desktop publishing software like Aldus PageMaker including versions of Lorem Ipsum.</p>
      <p>Lorem Ipsum is simply dummy text of the printing and typesetting industry. Lorem Ipsum has been the industry's standard dummy text ever since the 1500s, when an unknown printer took a galley of type and scrambled it to make a type specimen book. It has survived not only five centuries, but also the leap into electronic typesetting, remaining essentially unchanged. It was popularised in the 1960s with the release of Letraset sheets containing Lorem Ipsum passages, and more recently with desktop publishing software like Aldus PageMaker including versions of Lorem Ipsum.</p>
    </article>

    <section class="signature">
      <h3>Clara Wendell</h3>
      <p>Creative Designer</p>
    </section>

    <footer>
      <p class="footer-address">Address: Suite 9, 14 Harbour Lane, Kelston ACT 5810 &nbsp;ABN: 12 345 678 900</p>
      <div class="footer-band">
        <span class="stripe" style="left:28px"></span>
        <span class="stripe" style="left:40px"></span>
        <span class="stripe" style="right:40px"></span>
        <span class="stripe" style="right:56px"></span>
        <span class="stripe" style="right:76px;width:14px"></span>
      </div>
    </footer>
  </main>
</body>
</html>
```